Boston area Multi-store hair salon needs a poster for a special service

We need a poster for a soon to be multi-store hair salon based in the Boston area. We are expanding, opening more salons. We need a poster for a service we offer called "The Full Trim!" It is for men, and it includes:
1. Haircut
2. Shampoo
3. Neck Shave
4. Hot Towel Service

We charge $22 for The Full Trim!
70% of our clients are men.
Our website is www.mapleshears-demo.net
Our colors are black and red
***Please focus on the "The Full Trim!" part of the poster. We are almost looking for logo or icon for The Full Trim! part. *****
This will be hung inside the store near the reception area and possibly through out the salon and could be included in emails.
I have attached our logo and some other branding items we use (business cards, rewards cards, envelopes, etc) to help give you an idea of the look and feel we currently have. I have also attached an ad from Halvex which is a coupon they use for a service they call the full trim, just to give an idea. We like how Halvex created "The Full Trim" as an icon or logo.

Target Market(s)

Men

Industry/Entity Type

Store

Requirements
Nice to have
• Pictures of each service. We uploaded some examples.
• Also, "The Full Trim!" should be like a logo/icon

```html
<!DOCTYPE html>
<html lang="en">
<head>
<meta charset="utf-8">
<title>The Full Trim! – Maple Shears</title>
<link rel="stylesheet" href="https://fonts.googleapis.com/css2?family=Archivo+Black&family=Roboto:wght@900&family=Oswald:wght@700&display=swap">
<style>
  :root {
    --red: #d0202e;
    --red-dark: #a8121d;
    --black: #111111;
    --white: #ffffff;
    --frame: #e8e8e8;
  }
  * { margin: 0; padding: 0; box-sizing: border-box; }
  html, body { width: 900px; height: 1200px; overflow: hidden; }
  body { font-family: "Archivo Black", sans-serif; }

  .poster {
    position: relative;
    width: 900px;
    height: 1200px;
    background: var(--red);
    overflow: hidden;
  }
  .poster__sweep { position: absolute; inset: 0; }

  .headline { position: absolute; left: 30px; top: 0; line-height: 1; }
  .headline__get {
    position: absolute; left: 20px; top: 12px;
    font-size: 112px; color: var(--white);
    text-shadow: 2px 3px 4px rgba(0,0,0,.35);
  }
  .headline__the {
    position: absolute; left: 110px; top: 118px;
    font-size: 128px; color: var(--black);
  }
  .headline__title {
    position: absolute; left: 8px; top: 238px;
    font-size: 122px; color: var(--black);
    white-space: nowrap; letter-spacing: -2px;
  }
  .headline__title .outline {
    color: var(--red);
    -webkit-text-stroke: 12px var(--black);
    paint-order: stroke fill;
  }

  .brand {
    position: absolute; left: 470px; top: 178px;
    display: flex; align-items: center; gap: 10px;
  }
  .brand__dot { width: 22px; height: 22px; border-radius: 50%; background: var(--red); }
  .brand__name {
    font-family: "Archivo Black", sans-serif;
    font-size: 30px; color: var(--black); letter-spacing: 1px;
  }

  .for-men {
    position: absolute; left: 486px; top: 378px;
    font-family: "Archivo Black", sans-serif;
    font-size: 60px; color: var(--red);
    text-shadow: 1px 2px 3px rgba(0,0,0,.3);
  }

  .photos { position: absolute; left: 103px; top: 383px; display: flex; flex-direction: column; gap: 14px; }
  .photo {
    width: 188px; height: 188px;
    border: 3px solid var(--frame);
  }
  .photo--shampoo { background: linear-gradient(135deg, #3a3230, #d9c6b0 55%, #2b2b2b); }
  .photo--haircut { background: linear-gradient(160deg, #1d1a18, #c9a070 50%, #e2c08c); }
  .photo--towel { background: linear-gradient(180deg, #3a3a3a, #c9a87c 40%, #b08a60 75%, #2a2a2a); }
  .photo--shave { background: linear-gradient(135deg, #b99a6f, #e6cfae 55%, #f4efe8); }

  .benefits { position: absolute; left: 345px; top: 520px; }
  .benefits__title {
    margin-left: 140px;
    font-size: 44px; color: var(--red); margin-bottom: 8px;
  }
  .benefits__list { list-style: none; }
  .benefits__item {
    display: flex; align-items: center; gap: 8px;
    height: 60px;
    font-family: "Roboto", Arial, sans-serif; font-weight: 900;
    font-size: 44px; color: var(--black);
  }
  .benefits__tick { width: 46px; height: 46px; flex: none; }

  .price {
    position: absolute; left: 458px; top: 858px;
    width: 300px; height: 300px; border-radius: 50%;
    background: var(--red); color: var(--white);
    font-family: "Oswald", sans-serif; text-transform: uppercase;
    text-shadow: 2px 3px 4px rgba(0,0,0,.35);
  }
  .price__lead { position: absolute; left: 26px; top: 72px; font-size: 50px; line-height: 48px; }
  .price__amount { position: absolute; left: 26px; top: 168px; font-size: 118px; line-height: 1; }
  .price__currency, .price__cents { font-size: 50px; vertical-align: top; position: relative; top: 8px; }
</style>
</head>
<body>
<main class="poster">
  <svg class="poster__sweep" width="900" height="1200" viewBox="0 0 900 1200" aria-hidden="true">
    <path d="M420 0 C280 200 190 420 205 640 C220 860 300 1060 430 1200 L900 1200 L900 0 Z" fill="#ffffff"/>
  </svg>

  <h1 class="headline">
    <span class="headline__get">GET</span>
    <span class="headline__the">THE</span>
    <span class="headline__title">F<span class="outline">U</span>LL T<span class="outline">R</span>IM<span class="outline">!</span></span>
  </h1>

  <div class="brand">
    <span class="brand__dot"></span>
    <span class="brand__name">MAPLE SHEARS</span>
  </div>

  <p class="for-men">FOR MEN</p>

  <div class="photos">
    <div class="photo photo--shampoo" role="img" aria-label="Photo of a man receiving a shampoo at a basin"></div>
    <div class="photo photo--haircut" role="img" aria-label="Photo of a stylist cutting hair with scissors"></div>
    <div class="photo photo--towel" role="img" aria-label="Photo of a hot towel wrapped over a client's face"></div>
    <div class="photo photo--shave" role="img" aria-label="Photo of a neck shave with a straight razor"></div>
  </div>

  <section class="benefits">
    <h2 class="benefits__title">YOU GET:</h2>
    <ul class="benefits__list">
      <li class="benefits__item"><svg class="benefits__tick" viewBox="0 0 46 46" aria-hidden="true"><rect x="3" y="16" width="24" height="24" fill="none" stroke="#111" stroke-width="4"/><path d="M6 22 L15 32 L38 4" fill="none" stroke="#d0202e" stroke-width="7" stroke-linejoin="round"/></svg>Shampoo</li>
      <li class="benefits__item"><svg class="benefits__tick" viewBox="0 0 46 46" aria-hidden="true"><rect x="3" y="16" width="24" height="24" fill="none" stroke="#111" stroke-width="4"/><path d="M6 22 L15 32 L38 4" fill="none" stroke="#d0202e" stroke-width="7" stroke-linejoin="round"/></svg>Haircut</li>
      <li class="benefits__item"><svg class="benefits__tick" viewBox="0 0 46 46" aria-hidden="true"><rect x="3" y="16" width="24" height="24" fill="none" stroke="#111" stroke-width="4"/><path d="M6 22 L15 32 L38 4" fill="none" stroke="#d0202e" stroke-width="7" stroke-linejoin="round"/></svg>Hot Towel Service</li>
      <li class="benefits__item"><svg class="benefits__tick" viewBox="0 0 46 46" aria-hidden="true"><rect x="3" y="16" width="24" height="24" fill="none" stroke="#111" stroke-width="4"/><path d="M6 22 L15 32 L38 4" fill="none" stroke="#d0202e" stroke-width="7" stroke-linejoin="round"/></svg>Neck Shave</li>
    </ul>
  </section>

  <div class="price">
    <p class="price__lead">All for<br>only</p>
    <p class="price__amount"><span class="price__currency">$</span>22<span class="price__cents">00</span></p>
  </div>
</main>
</body>
</html>
```